Business Card for Bloom Vitality & Strength

Hi can you please design a business card with my logo and program logo (the new one I just sent) somewhere on it too maybe on the back? Needs to be eye catching and super cool.
Trudy Melcombe, Director
Master Personal Trainer & Nutrition Coach
0472 816 305
Www.bloomvitalitystrength.com.au
Insta (logo) bloom_vitality_strength #bloomyou7x72018

Target Market(s)

30+ women looking to change lifestyle to healthy mind body etc

Industry/Entity Type

Health And Wellness

Contact Information for Business Card

As above

Font styles to use
Sans Serif

Colors

Designer to choose colors to be used in the design.

Requirements
Must have
• Must super cool and edgy with a bit of cuteness

```html
<!DOCTYPE html>
<html lang="en">
<head>
<meta charset="utf-8">
<title>Bloom Vitality &amp; Strength – Business Card</title>
<link rel="stylesheet" href="https://fonts.googleapis.com/css2?family=Montserrat:wght@400;500;700;800&family=Oswald:wght@600&display=swap">
<style>
  :root {
    --bg: #e7e4df;
    --red: #d71f1f;
    --green: #1fa84a;
    --ink: #141414;
    --paper: #ffffff;
    --mist: #eef6fa;
    --photo-dark: #1f2a33;
    --photo-warm: #7a4a33;
  }
  html, body {
    margin: 0;
    width: 1200px;
    height: 1200px;
    overflow: hidden;
    background: var(--bg);
    font-family: "Montserrat", sans-serif;
  }
  .stage {
    position: relative;
    width: 1200px;
    height: 1200px;
  }
  .card {
    position: absolute;
    left: 120px;
    width: 960px;
    height: 548px;
    box-shadow: 0 10px 28px rgba(0,0,0,.18);
    overflow: hidden;
  }
  .card--front { top: 40px; background: var(--mist); }
  .card--back { top: 612px; background: var(--paper); }
  .card svg.art { position: absolute; inset: 0; width: 100%; height: 100%; }

  .front-title {
    position: absolute;
    left: 440px;
    top: 62px;
    color: var(--paper);
    font-weight: 700;
    font-size: 26px;
    letter-spacing: 2px;
  }
  .front-title .spaced {
    display: block;
    color: var(--green);
    font-weight: 500;
    font-size: 20px;
    letter-spacing: 14px;
    margin-top: 2px;
    padding-left: 70px;
  }

  .brand {
    position: absolute;
    display: flex;
    align-items: center;
    gap: 12px;
    color: var(--ink);
    font-weight: 800;
    line-height: 1.2;
  }
  .brand__dot { border-radius: 50%; background: var(--red); flex: none; }
  .brand--small { left: 680px; top: 290px; width: 240px; font-size: 20px; }
  .brand--small .brand__dot { width: 30px; height: 30px; }
  .brand--large { left: 110px; top: 420px; font-size: 36px; white-space: nowrap; }
  .brand--large .brand__dot { width: 58px; height: 58px; }

  .identity {
    position: absolute;
    left: 330px;
    top: 92px;
    width: 460px;
    text-align: center;
  }
  .identity__name {
    font-family: "Oswald", sans-serif;
    font-weight: 600;
    font-size: 48px;
    letter-spacing: -1px;
    line-height: 1;
    color: var(--ink);
    text-transform: uppercase;
  }
  .identity__name .surname { color: var(--red); }
  .identity__role {
    font-size: 19px;
    letter-spacing: 3px;
    margin-top: 4px;
    color: var(--ink);
  }
  .identity__rule { height: 3px; background: var(--green); margin: 10px 0 10px; }
  .identity__title { font-size: 17px; letter-spacing: 1.5px; color: var(--ink); }

  .contacts {
    position: absolute;
    left: 500px;
    top: 250px;
    list-style: none;
    margin: 0;
    padding: 0;
    font-size: 20px;
    color: var(--ink);
    white-space: nowrap;
  }
  .contacts li { display: flex; align-items: center; gap: 16px; margin-bottom: 12px; }
  .contacts svg { width: 26px; height: 26px; flex: none; }
</style>
</head>
<body>
<main class="stage">

  <section class="card card--front">
    <svg class="art" viewBox="0 0 960 548">
      <path d="M0 0 H960 V30 C640 220 560 420 380 548 H0 Z" fill="var(--red)"/>
      <defs>
        <linearGradient id="photoTone" x1="0" y1="0" x2="1" y2="1">
          <stop offset="0" stop-color="var(--photo-dark)"/>
          <stop offset="0.6" stop-color="var(--photo-warm)"/>
          <stop offset="1" stop-color="var(--photo-dark)"/>
        </linearGradient>
      </defs>
      <path role="img" aria-label="Photo of two athletes training with dumbbells"
            d="M0 0 H350 C420 140 520 200 620 212 C560 330 480 460 380 548 H0 Z"
            fill="url(#photoTone)"/>
      <path d="M960 30 C640 220 560 420 380 548" fill="none" stroke="var(--green)" stroke-width="16"/>
    </svg>
    <div class="front-title">BLOOM VITALITY &amp;<span class="spaced">STRENGTH</span></div>
    <div class="brand brand--small"><span class="brand__dot"></span>BLOOM VITALITY &amp; STRENGTH</div>
  </section>

  <section class="card card--back">
    <div class="identity">
      <div class="identity__name">Trudy <span class="surname">Melcombe</span></div>
      <div class="identity__role">DIRECTOR</div>
      <div class="identity__rule"></div>
      <div class="identity__title">Master Personal Trainer &amp; Nutrition Coach</div>
    </div>

    <ul class="contacts">
      <li>
        <svg viewBox="0 0 24 24"><path fill="var(--red)" d="M6.6 10.8a15 15 0 0 0 6.6 6.6l2.2-2.2c.3-.3.7-.4 1-.2 1.1.4 2.3.6 3.6.6.6 0 1 .4 1 1V20c0 .6-.4 1-1 1A17 17 0 0 1 3 4c0-.6.4-1 1-1h3.5c.6 0 1 .4 1 1 0 1.3.2 2.5.6 3.6.1.3 0 .7-.2 1z"/></svg>
        <span>0472 816 305</span>
      </li>
      <li>
        <svg viewBox="0 0 24 24" fill="none" stroke="var(--red)" stroke-width="2"><circle cx="12" cy="12" r="9"/><ellipse cx="12" cy="12" rx="4" ry="9"/><path d="M3 12h18M5 7h14M5 17h14"/></svg>
        <span>www.bloomvitalitystrength.com.au</span>
      </li>
      <li>
        <svg viewBox="0 0 24 24"><circle cx="12" cy="12" r="9" fill="var(--red)"/></svg>
        <span>bloom_vitality_strength</span>
      </li>
    </ul>

    <div class="brand brand--large"><span class="brand__dot"></span>BLOOM VITALITY &amp; STRENGTH</div>
  </section>

</main>
</body>
</html>
```